New website for Pollard Law Firm at www.keepwinning-example.com

We are a professional law firm located in the Nashville, Tennessee USA area. We focus on personal injury law. We are looking for a slick new website that is user friendly for updating with new blogs, videos, etc. The primary colors should be red, black, and white. It should load extremely fast and have a good mobile component. The pages for the design will include a home page, about us, news, contact us, and practice page. The practice page will be copied for all the practice areas including motor vehicle accidents, slip and fall accidents, dog bites, etc. We have included an image which we would like to include in the new site which shows the color scheme The image is called banner-Car Wreck. The new website should NOT have gavels, court houses, law books, scales or the typical images for a law firm.

Target Market(s)

People in Tennessee involved in accidents

Industry/Entity Type

Legal services, law firm

Coding

Coded - Design and coding required

Number of Pages Required

5+ page

Font styles to use
Serif

Colors
EB3D1F
EC4F4E
F09395
F8D3D4
FCEDEE

Requirements
Should not have
• Gavels, columns, scales, law related images

```html
<!DOCTYPE html>
<html lang="en">
<head>
<meta charset="utf-8">
<title>Pollard Law Firm – About Us</title>
<link href="https://fonts.googleapis.com/css2?family=Open+Sans:wght@300;400;600&display=swap" rel="stylesheet">
<style>
:root{
  --red:#c8232c;
  --red-soft:#d23a3f;
  --dark-red:#a81c22;
  --ink:#333;
  --muted:#777;
  --line:#e6e6e6;
  --footer:#444;
  --white:#fff;
  --gold:#c9a227;
}
*{margin:0;padding:0;box-sizing:border-box}
html,body{width:1200px;height:3462px;overflow:hidden}
body{position:relative;background:var(--white);font-family:"Open Sans",Arial,sans-serif;color:var(--ink)}
.abs{position:absolute}
a{color:inherit;text-decoration:none}

/* header */
.brand{left:125px;top:42px;color:var(--red);font-weight:400;text-align:center;line-height:1}
.brand .name{font-size:34px;letter-spacing:1px;display:block}
.brand .sub{font-size:15px;letter-spacing:1px;display:block;margin-top:3px}
.nav{top:60px;left:540px;display:flex;gap:0;font-size:12px;color:#444}
.nav a{position:absolute;white-space:nowrap}
.nav a.active{color:var(--red);border-bottom:1px solid var(--red);padding-bottom:5px}
.search{left:920px;top:58px}
.divider{left:957px;top:56px;width:1px;height:22px;background:#999}
.phone-top{left:970px;top:58px;font-size:15px;color:#555}

/* hero */
.hero{left:0;top:122px;width:1200px;height:553px;background:linear-gradient(100deg,#c9ced3 0%,#9aa2a9 35%,#5b636b 65%,#2d3238 100%)}
.hero h1{position:absolute;left:125px;top:248px;font-size:32px;font-weight:300;color:var(--white);letter-spacing:1px}

/* section heads */
.eyebrow{width:1200px;left:0;text-align:center;font-size:11px;color:var(--muted)}
.heading{width:1200px;left:0;text-align:center;font-size:29px;font-weight:400;letter-spacing:1.5px;color:#333}
.heading span{color:var(--red)}
.lead{left:400px;width:400px;text-align:center;font-size:11.5px;line-height:22px;color:var(--muted)}

/* intro columns */
.col-title{font-size:29px;font-weight:400;letter-spacing:1px;color:#333}
.rule{width:30px;height:1px;background:var(--red)}
.col-text{width:440px;font-size:11.5px;line-height:22px;color:var(--muted)}
.btn{height:39px;border-radius:20px;background:var(--red);color:var(--white);font-size:12px;display:flex;align-items:center;justify-content:center;gap:22px}
.btn .dot{width:23px;height:23px;border-radius:50%;background:#111;display:flex;align-items:center;justify-content:center}

/* stats band */
.band{left:0;top:1293px;width:1200px;height:496px}
.stat{width:214px;height:204px;background:var(--white);border-radius:6px;text-align:center}
.stat svg{margin-top:26px}
.stat .label{font-size:18px;color:#333;margin-top:14px}
.stat .value{font-size:22px;color:#555;margin-top:8px;letter-spacing:1px}

/* attorneys */
.attorney{width:299px;height:390px;border-radius:6px;overflow:hidden}
.attorney .photo{height:308px;background:linear-gradient(180deg,#d9dadc,#9ea3a9)}
.attorney .plate{height:82px;background:var(--red);color:var(--white);text-align:center;padding-top:20px}
.attorney.featured .plate{background:#000}
.plate .who{font-size:19px}
.plate .role{font-size:11px;margin-top:6px;letter-spacing:.3px}

/* feedback */
.review{width:297px;height:231px;border:1px solid #eee;border-radius:8px;text-align:center;padding-top:66px}
.avatar{width:78px;height:78px;border-radius:50%;background:linear-gradient(160deg,#c7cbd0,#7e868e)}
.review .who{font-size:13px;color:#333}
.review .role{font-size:12px;color:var(--muted);margin-top:6px}
.review p{font-size:12px;line-height:16px;color:#555;margin:18px auto 0;width:245px}
.stars{margin-top:16px;color:var(--gold);font-size:14px;letter-spacing:3px}
.pager{top:2920px;width:13px;height:13px;border-radius:50%;background:var(--red)}
.pager.off{background:var(--white);border:1.5px solid var(--red)}

/* footer */
.footer{left:0;top:3031px;width:1200px;height:360px;background:var(--footer);color:var(--white)}
.footer .brand{color:var(--white);top:95px}
.f-head{font-size:13px;color:var(--white)}
.f-head::after{content:"";display:block;width:28px;height:1px;background:var(--white);margin-top:5px}
.f-text{font-size:11.5px;line-height:20px}
.f-links{font-size:12px}
.f-links li{list-style:none;height:31px}
.f-links li::before{content:"→";font-size:9px;margin-right:8px}
.input{width:180px;height:37px;border-radius:19px;background:var(--white);color:#777;font-size:10px;padding:12px 18px}
.subscribe{width:180px;height:37px;border-radius:19px;background:var(--red);color:var(--white);font-size:9px;text-align:center;line-height:37px}
.map{width:199px;height:135px;border:3px solid var(--white);background:linear-gradient(135deg,#dfe7d6,#c8d6e4)}
.copyright{left:125px;top:3414px;font-size:12px;color:#444}
.copyright span{color:var(--red)}
.social{top:3406px;width:27px;height:27px;border-radius:50%}
</style>
</head>
<body>

<!-- header -->
<div class="abs brand"><span class="name">POLLARD</span><span class="sub">LAW FIRM PLLC</span></div>
<nav class="abs nav" style="left:0">
  <a style="left:540px">Home</a>
  <a class="active" style="left:601px">About us</a>
  <a style="left:677px">Practice Areas</a>
  <a style="left:781px">News</a>
  <a style="left:839px">Contact us</a>
</nav>
<svg class="abs search" width="17" height="17" viewBox="0 0 17 17"><circle cx="7" cy="7" r="5.5" fill="none" stroke="#666" stroke-width="1.3"/><line x1="11" y1="11" x2="16" y2="16" stroke="#666" stroke-width="1.3"/></svg>
<div class="abs divider"></div>
<div class="abs phone-top">(615) 555-0147</div>

<!-- hero -->
<section class="abs hero" role="img" aria-label="Photo of two people at a desk signing a document">
  <h1>ABOUT US</h1>
</section>

<!-- intro -->
<div class="abs eyebrow" style="top:748px">About us</div>
<h2 class="abs heading" style="top:772px">WE ARE RIGHT <span>FIRM</span></h2>
<p class="abs lead" style="top:822px">Lorem Lorem Ipsum a available, but the majority have suffered alter ation dolor amet simple dunny text</p>

<div class="abs" style="left:125px;top:926px">
  <h3 class="col-title">Trial Lawyers</h3>
  <div class="rule" style="margin-top:18px"></div>
  <p class="col-text" style="margin-top:12px">WE ARE TRIAL LAWYERS AND WE ARE PROUD OF IT! There are many law firms in Tennessee who claim to be trial lawyers, but their attorneys have never seen a courtroom. We have tried hundreds of cases to verdict and we have helped thousands of people in the Tennessee courts. We fight against billion dollar insurance companies, billion dollar corporations, and the State of Tennessee..and we win!</p>
</div>
<a class="abs btn" style="left:125px;top:1146px;width:159px">Read More <span class="dot"><svg width="9" height="9" viewBox="0 0 9 9"><path d="M3 1l3.5 3.5L3 8" fill="none" stroke="#fff" stroke-width="1.5"/></svg></span></a>

<div class="abs" style="left:638px;top:922px">
  <h3 class="col-title">History</h3>
  <div class="rule" style="margin-top:18px"></div>
  <p class="col-text" style="margin-top:12px;width:437px">The Pollard Law Firm began in 2005 when Mr. Pollard graduated from law school and wanted nothing more than to become a trial lawyer. At the time, he only had enough money to rent a small one room office in downtown Nashville and the only furniture he could afford was a few bankers boxes, a laptop, and a small plastic chair. It was certainly risky, but he somehow knew that it would work.</p>
</div>
<a class="abs btn" style="left:638px;top:1146px;width:159px">Read More <span class="dot"><svg width="9" height="9" viewBox="0 0 9 9"><path d="M3 1l3.5 3.5L3 8" fill="none" stroke="#fff" stroke-width="1.5"/></svg></span></a>

<!-- stats band -->
<svg class="abs band" width="1200" height="496" viewBox="0 0 1200 496" role="img" aria-label="Red tinted band with a blurred office photo">
  <defs><linearGradient id="bandFill" x1="0" y1="0" x2="1" y2="1"><stop offset="0" stop-color="#d23a3f"/><stop offset="1" stop-color="#b8252b"/></linearGradient></defs>
  <polygon points="0,105 1200,0 1200,496 0,496" fill="url(#bandFill)"/>
  <polygon points="1164,3 1200,0 1200,496 1164,496" fill="#c21d24"/>
</svg>

<div class="abs stat" style="left:125px;top:1485px">
  <svg width="70" height="68" viewBox="0 0 70 68" fill="none" stroke="#c8232c" stroke-width="2"><rect x="3" y="34" width="11" height="30"/><path d="M14 38 26 22V8c6 0 9 5 8 14h16c4 0 6 4 4 7 2 2 2 6-1 8 2 3 0 6-3 7 1 3-1 6-5 6H26l-12-4"/><path d="M52 2l3 7 7 1-5 5 1 7-6-3-6 3 1-7-5-5 7-1z"/></svg>
  <div class="label">Satisfied Client</div><div class="value">1250</div>
</div>
<div class="abs stat" style="left:371px;top:1485px">
  <svg width="76" height="68" viewBox="0 0 76 68" fill="none" stroke="#c8232c" stroke-width="2"><path d="M2 18l12 14 8-6 10 12 10 10c3 3 7 0 5-3"/><path d="M74 18 62 32l-6-4-14-12-10 6c-4 2-7-2-4-5l12-10h12l10 8"/><path d="M28 44l6 6M22 48l6 6M36 40l8 8"/></svg>
  <div class="label">Total Case Won</div><div class="value">428</div>
</div>
<div class="abs stat" style="left:617px;top:1485px">
  <svg width="60" height="72" viewBox="0 0 60 72" fill="none" stroke="#c8232c" stroke-width="2"><circle cx="30" cy="26" r="22"/><circle cx="30" cy="26" r="15"/><path d="M23 26l5 5 9-10"/><path d="M16 44 10 66l9-4 5 8 6-20M44 44l6 22-9-4-5 8-6-20"/></svg>
  <div class="label">Honor &amp; Award</div><div class="value">385</div>
</div>
<div class="abs stat" style="left:861px;top:1485px">
  <svg width="64" height="72" viewBox="0 0 64 72" fill="none" stroke="#c8232c" stroke-width="2"><circle cx="32" cy="20" r="14"/><path d="M4 70V54c0-8 8-14 16-14h24c8 0 16 6 16 14v16z"/><path d="M26 40l6 12 6-12M32 52v18"/></svg>
  <div class="label">Number of Lawyer</div><div class="value">350</div>
</div>

<!-- attorneys -->
<div class="abs eyebrow" style="top:1882px">Our Expert</div>
<h2 class="abs heading" style="top:1905px">OUR ATTORNEYS</h2>

<div class="abs attorney" style="left:125px;top:1969px">
  <div class="photo" role="img" aria-label="Portrait photo of attorney"></div>
  <div class="plate"><div class="who">Daniel R. Pollard</div><div class="role">ATTORNEY</div></div>
</div>
<div class="abs attorney featured" style="left:450px;top:1969px">
  <div class="photo" role="img" aria-label="Portrait photo of litigation paralegal"></div>
  <div class="plate"><div class="who">Martin E. Hale</div><div class="role">LITIGATION PARALEGAL</div></div>
</div>
<div class="abs attorney" style="left:776px;top:1969px">
  <div class="photo" role="img" aria-label="Portrait photo of legal assistant"></div>
  <div class="plate"><div class="who">Paula Lindqvist</div><div class="role">LEGAL ASSISTANT</div></div>
</div>
<a class="abs btn" style="left:521px;top:2412px;width:159px">View More <span class="dot"><svg width="9" height="9" viewBox="0 0 9 9"><path d="M3 1l3.5 3.5L3 8" fill="none" stroke="#fff" stroke-width="1.5"/></svg></span></a>

<!-- feedback -->
<div class="abs eyebrow" style="top:2506px">Client Love us</div>
<h2 class="abs heading" style="top:2530px">CLIENT FEEDBACK</h2>

<div class="abs review" style="left:125px;top:2652px">
  <div class="who">Christian</div><div class="role">Creative Director</div>
  <p>Lorem Ipsum is simply dummy text of the printing and typesetting industry has been the industry's standard.</p>
  <div class="stars">★★★★★</div>
</div>
<div class="abs review" style="left:451px;top:2652px">
  <div class="who">Sandra Moss</div><div class="role">Creative Director</div>
  <p>Lorem Ipsum is simply dummy text of the printing and typesetting industry has been the industry's standard.</p>
  <div class="stars">★★★★☆</div>
</div>
<div class="abs review" style="left:777px;top:2652px">
  <div class="who">Mark Verlin</div><div class="role">Creative Director</div>
  <p>Lorem Ipsum is simply dummy text of the printing and typesetting industry has been the industry's standard.</p>
  <div class="stars">★★★★★</div>
</div>
<div class="abs avatar" style="left:235px;top:2611px" role="img" aria-label="Client photo"></div>
<div class="abs avatar" style="left:561px;top:2611px" role="img" aria-label="Client photo"></div>
<div class="abs avatar" style="left:888px;top:2611px" role="img" aria-label="Client photo"></div>

<div class="abs pager off" style="left:577px"></div>
<div class="abs pager" style="left:595px"></div>
<div class="abs pager" style="left:614px"></div>

<!-- footer -->
<footer class="abs footer">
  <div class="abs brand" style="left:125px"><span class="name">POLLARD</span><span class="sub">LAW FIRM PLLC</span></div>

  <svg class="abs" style="left:125px;top:164px" width="13" height="17" viewBox="0 0 13 17"><path d="M6.5 0A6.5 6.5 0 0 0 0 6.5C0 11 6.5 17 6.5 17S13 11 13 6.5A6.5 6.5 0 0 0 6.5 0z" fill="#fff"/><circle cx="6.5" cy="6.5" r="2.3" fill="#444"/></svg>
  <p class="abs f-text" style="left:150px;top:160px;width:230px">1450 Birchwood Lane | Suite 210 | Franklin, TN 37000</p>
  <svg class="abs" style="left:125px;top:228px" width="13" height="13" viewBox="0 0 13 13"><path d="M3 0l2 3-1.5 1.8c.8 1.8 2.4 3.4 4.2 4.2L9.5 7.5 13 9.5 11.5 13C5 12.5.5 8 0 1.5z" fill="#fff"/></svg>
  <div class="abs f-text" style="left:150px;top:224px">(615) 555-0147</div>
  <svg class="abs" style="left:125px;top:250px" width="15" height="11" viewBox="0 0 15 11"><rect width="15" height="11" fill="#fff"/><path d="M0 0l7.5 6L15 0" fill="none" stroke="#444" stroke-width="1.3"/></svg>
  <div class="abs f-text" style="left:152px;top:245px">office@pollardlaw-example.com</div>

  <div class="abs f-head" style="left:443px;top:90px">Quick Link</div>
  <ul class="abs f-links" style="left:443px;top:124px">
    <li>Home</li><li>About us</li><li>Practice Areas</li><li>News</li><li>Contact us</li>
  </ul>

  <div class="abs f-head" style="left:636px;top:90px">Newsletter</div>
  <p class="abs f-text" style="left:636px;top:124px;width:190px;line-height:17px">Join Our Newsletter To Receive The Latest Update.</p>
  <div class="abs input" style="left:632px;top:185px">Your Email</div>
  <div class="abs subscribe" style="left:632px;top:232px">SUBSCRIBE</div>

  <div class="abs f-head" style="left:876px;top:90px">Map</div>
  <div class="abs map" style="left:876px;top:134px" role="img" aria-label="Map showing the office location"></div>
</footer>

<div class="abs copyright">Copyright © 2021 <span>POLLARD LAW FIRM PLLC</span>, All Rights Reserved.</div>
<div class="abs social" style="left:934px;background:var(--red)" aria-label="Social link"></div>
<div class="abs social" style="left:972px;background:#444" aria-label="Social link"></div>
<div class="abs social" style="left:1010px;background:#444" aria-label="Social link"></div>
<div class="abs social" style="left:1048px;background:#444" aria-label="Social link"></div>

</body>
</html>
```